Bluestone Auto Works | ||
Bluestone | ||
Automotive | ||
Bluestone Auto Works is a auto reseller, that offers consignment, brokerage, and restoration services. | ||
Like black back grounds, dislike hookey websites | ||
Cutting-Edge Professional Trendy Sophisticated Modern Elegant Progressive Service Oriented High Tech Masculine |
black backgroung | ||
left side | ||
www.dravelkustom.com | ||
http://www.harborlinebuilds.com/ | ||
http://www.ridgefieldcycleworks.com/ | ||
used logo to coordinate colors | ||

```html
<!DOCTYPE html>
<html lang="en">
<head>
<meta charset="utf-8">
<title>Bluestone Auto Works</title>
<link href="https://fonts.googleapis.com/css2?family=Arimo:wght@400;700&display=swap" rel="stylesheet">
<style>
  :root {
    --orange: #f26a10;
    --orange-dark: #b8440a;
    --page: #141414;
    --panel: #1d1d1d;
    --panel-dark: #0d0d0d;
    --text: #e6e6e6;
    --muted: #9a9a9a;
    --line: #3a3a3a;
  }
  * { margin: 0; padding: 0; box-sizing: border-box; }
  html, body { width: 1200px; height: 923px; overflow: hidden; }
  body {
    position: relative;
    font-family: "Arimo", Arial, sans-serif;
    color: var(--text);
    background:
      repeating-linear-gradient(45deg, rgba(255,255,255,0.025) 0 2px, transparent 2px 5px),
      repeating-linear-gradient(-45deg, rgba(0,0,0,0.25) 0 2px, transparent 2px 5px),
      radial-gradient(ellipse at 50% 30%, #2a2a2a 0%, var(--page) 70%);
  }
  .top-rule { position: absolute; left: 0; top: 0; width: 1200px; height: 7px; background: var(--orange); }
  .nav-tab { position: absolute; left: 437px; top: 0; width: 30px; height: 50px; background: var(--orange); }

  .brand { position: absolute; left: 142px; top: 66px; display: flex; align-items: center; gap: 8px; white-space: nowrap; }
  .brand-dot { width: 26px; height: 26px; border-radius: 50%; background: var(--orange); flex: none; }
  .brand-name { font-size: 19px; font-weight: 700; color: #ffffff; }

  .main-nav { position: absolute; top: 73px; left: 432px; display: flex; font-size: 16px; white-space: nowrap; }
  .main-nav a { color: #ffffff; text-decoration: none; padding-right: 20px; margin-right: 20px; border-right: 1px solid #cccccc; line-height: 17px; }
  .main-nav a:last-child { border-right: 0; padding-right: 0; margin-right: 0; }
  .main-nav a.active { color: var(--orange); }

  .hero { position: absolute; left: 142px; top: 142px; width: 913px; height: 258px;
    background: linear-gradient(180deg, #eeeeee 0%, #c9c9c9 55%, #7a7a7a 80%, #2a2a2a 100%); }
  .hero-base { position: absolute; left: 142px; top: 400px; width: 913px; height: 22px; background: #3b3b3b; }
  .swoosh { position: absolute; left: 142px; top: 418px; width: 913px; height: 72px; }

  .sidebar { position: absolute; left: 142px; top: 487px; width: 195px; height: 313px;
    background: linear-gradient(180deg, var(--panel) 0%, #111 100%); }
  .brand-list { list-style: none; position: absolute; left: 28px; top: 11px; font-size: 16px; line-height: 23.2px; white-space: nowrap; }
  .brand-list li { color: #ffffff; }
  .brand-list li:nth-child(n+6) { color: var(--muted); }
  .slider-track { position: absolute; left: 151px; top: 13px; width: 3px; height: 285px; background: #5a5a5a; }
  .slider-knob { position: absolute; left: 144px; top: 80px; width: 17px; height: 36px; border-radius: 8px; border: 2px solid #777; background: #2c2c2c; }

  .section-title { position: absolute; left: 357px; font-size: 22px; font-weight: 400; color: #ffffff; }
  .thumb { position: absolute; }
  .copy { position: absolute; font-size: 13.5px; line-height: 20px; color: #dddddd; }
  .more { position: absolute; right: 145px; font-size: 16px; color: #ffffff; }
  .divider { position: absolute; left: 357px; top: 640px; width: 698px; height: 3px; background: var(--orange); }

  .site-footer { position: absolute; left: 0; top: 800px; width: 1200px; height: 123px; background: var(--panel-dark); }
  .footer-brand { position: absolute; left: 170px; top: 40px; font-size: 19px; font-weight: 700; color: #3c3c3c; white-space: nowrap; }
  .follow { position: absolute; left: 496px; top: 44px; font-size: 14px; color: #ffffff; white-space: nowrap; }
  .social { position: absolute; top: 33px; width: 30px; height: 30px; border-radius: 4px; background: var(--orange); }
  .copyright { position: absolute; left: 816px; top: 45px; font-size: 13px; color: #ffffff; white-space: nowrap; }
</style>
</head>
<body>
  <div class="top-rule"></div>
  <div class="nav-tab"></div>

  <header>
    <div class="brand"><span class="brand-dot"></span><span class="brand-name">Bluestone Auto Works</span></div>
    <nav class="main-nav">
      <a class="active" href="#">Home</a>
      <a href="#">About us</a>
      <a href="#">Services</a>
      <a href="#">New Cars</a>
      <a href="#">Accessories</a>
      <a href="#">Contact us</a>
    </nav>
  </header>

  <div class="hero" role="img" aria-label="Photo of a black luxury sedan in a bright studio"></div>
  <div class="hero-base"></div>
  <svg class="swoosh" viewBox="0 0 913 72" preserveAspectRatio="none" aria-hidden="true">
    <path d="M0 4 H913 V30 Q456 80 0 30 Z" fill="var(--orange)"/>
    <path d="M0 4 H913 V18 Q456 58 0 18 Z" fill="var(--orange-dark)" opacity="0.6"/>
  </svg>

  <aside class="sidebar">
    <ul class="brand-list">
      <li>Varenna Motori</li><li>Solvane</li><li>Ashby Marlowe</li><li>Avren</li>
      <li>Brockhurst</li><li>BKW</li><li>Brannic</li><li>Belcourt</li>
      <li>Castleford</li><li>Corvane</li><li>Ferrano</li><li>Gunthal</li>
    </ul>
    <div class="slider-track"></div>
    <div class="slider-knob"></div>
  </aside>

  <main>
    <h2 class="section-title" style="top:490px">New Cars</h2>
    <div class="thumb" style="left:357px;top:519px;width:229px;height:107px;background:linear-gradient(135deg,#6e6e6e,#5a0f14 55%,#1a1a1a)" role="img" aria-label="Photo of a dark red vintage coupe"></div>
    <p class="copy" style="left:604px;top:516px;width:451px">What is the most expensive car in the world? The 1931 Belcourt Regent Ardell Coupe was sold for $8,700,000 in 1987. However, that car and many alike will not be included in this list because it is not available on the market today. It is hard to imagine someone would actually spend 8 million dollars on a car instead of using it for something more</p>
    <span class="more" style="top:610px">more...</span>
    <div class="divider"></div>

    <h2 class="section-title" style="top:667px">Services</h2>
    <div class="thumb" style="left:357px;top:699px;width:72px;height:62px;background:linear-gradient(135deg,#9a9a9a,#3a3a3a 60%,#5a2010)" role="img" aria-label="Photo of a car in a workshop"></div>
    <p class="copy" style="left:449px;top:697px;width:606px">What is the most expensive car in the world? The 1931 Belcourt Regent Ardell Coupe was sold for $8,700,000 in 1987. However, that car and many alike will not be included in this list because it is not available on the market today.</p>
    <span class="more" style="top:766px">more...</span>
  </main>

  <footer class="site-footer">
    <div class="footer-brand">Bluestone Auto Works</div>
    <span class="follow">Follow us on</span>
    <span class="social" style="left:590px" aria-label="Social profile"></span>
    <span class="social" style="left:628px" aria-label="Social profile"></span>
    <span class="social" style="left:666px" aria-label="Video channel"></span>
    <span class="copyright">@2012 Bluestone Auto Works.com</span>
  </footer>
</body>
</html>
```